pathology learning flashcard template graphic design .

Creative designs for 2 sides of the flashcards to include colorful sectioning and font sizes that will make it easy to use in studying.

```html
<!DOCTYPE html>
<html lang="en">
<head>
<meta charset="utf-8">
<title>Pathology Flashcard – Gastrointestinal</title>
<link rel="stylesheet" href="https://fonts.googleapis.com/css2?family=Marmelad&family=Titillium+Web:wght@600;700&family=Open+Sans:ital,wght@0,400;0,700;1,400;1,700&display=swap">
<style>
  :root {
    --red: #d22a35;
    --white: #ffffff;
    --ink: #1d1d1d;
    --frame: #dcdcdc;
    --art: #e9c9a8;
  }
  * { box-sizing: border-box; margin: 0; padding: 0; }
  html, body { width: 846px; height: 1200px; overflow: hidden; background: var(--white); }
  body { position: relative; font-family: "Open Sans", sans-serif; color: var(--ink); }

  .card { position: absolute; left: 18px; width: 758px; border: 2px solid var(--frame); background: var(--white); overflow: hidden; }
  .card--case { top: 18px; height: 520px; }
  .card--answer { top: 590px; height: 520px; }

  /* Case card */
  .topic-art { position: absolute; left: 12px; top: 10px; width: 76px; height: 66px; border: 2px solid var(--red); background: linear-gradient(135deg, #f0d6b8, #e5b48e); }
  .topic-title { position: absolute; left: 98px; top: 8px; font-family: "Marmelad", sans-serif; font-weight: 400; font-size: 50px; line-height: 72px; color: var(--red); letter-spacing: 0.5px; }
  .accent-bar { position: absolute; right: 0; top: 0; width: 20px; height: 120px; background: var(--red); }
  .case-band { position: absolute; left: 0; top: 86px; width: 756px; height: 34px; background: var(--red); color: var(--white); font-family: "Titillium Web", sans-serif; font-weight: 700; font-size: 19px; line-height: 34px; padding-left: 14px; }

  .summary { position: absolute; left: 0; top: 120px; width: 257px; height: 398px; background: var(--red); padding: 0 2px; }
  .patient-art { width: 253px; height: 92px; margin-top: 2px; background: linear-gradient(180deg, #f4f4f4, #dcdcdc); }
  .summary dl { padding: 6px 10px 0; color: var(--white); font-size: 15.6px; line-height: 20.6px; }
  .summary dt { font-weight: 700; font-size: 13.5px; }
  .summary dd { font-style: italic; }

  .vignette { position: absolute; left: 270px; top: 126px; width: 467px; font-style: italic; font-size: 17.6px; line-height: 27.2px; text-align: justify; }
  .question { position: absolute; left: 270px; top: 420px; font-style: italic; font-weight: 700; font-size: 16.5px; }
  .options { position: absolute; left: 270px; top: 450px; width: 467px; border-collapse: collapse; font-style: italic; font-size: 15px; }
  .options td { border: 1.5px solid var(--red); height: 26px; padding: 0 5px; width: 50%; }
  .options b { font-weight: 700; }

  /* Answer card */
  .topic-band { position: absolute; left: 0; top: 0; width: 756px; height: 40px; background: var(--red); color: var(--white); font-style: italic; font-weight: 400; font-size: 20px; line-height: 42px; padding-left: 28px; }
  .notes { position: absolute; left: 28px; top: 52px; width: 702px; font-size: 13.3px; line-height: 24px; }
  .notes p { margin-bottom: 8px; }
  .label { color: var(--red); font-weight: 700; font-style: italic; }
  .explanation { position: absolute; left: 16px; top: 343px; width: 726px; height: 146px; border: 1.5px solid var(--red); padding: 3px 12px; font-style: italic; font-size: 12.9px; line-height: 22.5px; text-align: justify; }
  .explanation h3 { font-weight: 400; font-size: 13.5px; line-height: 20px; }
  .sources { position: absolute; left: 18px; top: 495px; font-size: 11.5px; }
  .page-no { position: absolute; left: 678px; top: 497px; font-size: 11.5px; }
</style>
</head>
<body>
  <section class="card card--case">
    <div class="topic-art" role="img" aria-label="Illustration of the stomach and digestive tract"></div>
    <h1 class="topic-title">GASTROINTESTINAL</h1>
    <div class="accent-bar"></div>
    <div class="case-band">PATHOLOGY CASE ID 0001</div>

    <aside class="summary">
      <div class="patient-art" role="img" aria-label="Cartoon of an older woman with glasses"></div>
      <dl>
        <dt>PATIENT</dt><dd>50-year-old woman;</dd>
        <dt>SYMPTOMS</dt><dd>Difficulty swallowing, cough,<br>Stopped eating many foods;<br>Weight lost ~12 lbs in&nbsp; 3 months;</dd>
        <dt>MEDICAL HISTORY</dt><dd>Unremarkable.Vital signs normal</dd>
        <dt>EXAMS</dt><dd>Physical exam is unremarkable;<br>Chest x-ray: air-fluid level;<br>Manometry: absent relaxation of<br>the lower esophageal sphincter<br>during swallowing;</dd>
      </dl>
    </aside>

    <p class="vignette">50-year-old woman comes to the clinic because she has difficulty swallowing for the past few months. She says symptoms have been worsening. She also complains of cough, mostly at night and in fear of choking, has stopped eating many foods, losing about 12 lbs in the past 3 months. Past medical history is unremarkable. Vital signs are normal and physical exam is unremarkable. Chest x-ray with demonstrates an air-fluid level, while manometry shows absent relaxation of the lower esophageal sphincter during swallowing.</p>
    <p class="question">What is the most likely diagnosis?</p>
    <table class="options">
      <tr><td><b>A)</b> GERD</td><td><b>B)</b> Barret Esophagus</td></tr>
      <tr><td><b>C)</b> Achalasia</td><td><b>D)</b> Eosinophilic esophagitis</td></tr>
    </table>
  </section>

  <section class="card card--answer">
    <h2 class="topic-band">ACHALASIA</h2>
    <div class="notes">
      <p><span class="label">DEFINITION</span> Motility disorder where esophageal relaxation is impaired in the lower esophageal sphincter (LES).</p>
      <p><span class="label">P/E AND SYMPTOMS</span> Dysphogia that is progressive, regurgitation, weight-loss, dry cough, chest pain, GERD, esophageal perforation, squomous cell carcinoma, aspiration pneumonia.</p>
      <p><span class="label">ETIOLOGY/PATHOLOGY</span> Destruction of inhibitory neurons in the Auerbach plexus. Manometry will present with increased resting lower esophageal Loss of peristalsis in the lower esophageal sphincter sphincter pressure. Endoscopy will usually present with normal (Lower-two thirds of the esophagus). mucosa and LES dilation, and in some cases residual material such as undigested food particles may be present.</p>
      <p><span class="label">DX</span> Barium swallow will show 'bird's beak' and esophageal dilation.</p>
      <p><span class="label">RX</span> First line of treatment are nitrates, calcium channel blockers, and Botulinum toxin injection in the LES. Long term management options include esophageal dilation with pneumatic balloon and myotomy.</p>
    </div>
    <div class="explanation">
      <h3>C) Achalasia</h3>
      <p>Symptoms and studies suggestive of achalasia. Patient's manometry presents with no relaxation of the lower esophageal sphincter during swallowing. Patient also complains of dysphagia and is unable to swallow properly, leading to weight loss. Patient has no past infection or inflammation, ruling out eosinophilic esophagitis. Patient does not have chronic GERD, eliminating the possibility of Barrett esophagus, in which at least 5 years of acid reflux are beforehand to develop columnar Lmetoplasia.</p>
    </div>
    <p class="sources">Sources:Harlow Drug Handbook;Brennick Pocket Formulary;medsreference.example;clinicnotes.example</p>
    <p class="page-no">1</p>
  </section>
</body>
</html>
```